Redesign vq7.ch agency website for unique design with speed and conversion

We want to redesign our website vq7.ch. Our omnichannel marketing agency builds webshops and integrates them into existing systems like ERP/CRM and supports with online marketing campaigns like brixel ads and social media. The target of the redesign is to get a great look and feel for customers to see directly what we do, (please design something for our three focus areas eCommerce, Online marketing and Integration)
and to improve the pages speed drastically for SEO. Please see our attachment.
Target Market(s)
B2B
Industry/Entity Type
eCommerce Agency
Coding
Coded - Design and coding required
Number of Pages Required
5+ page
Look and feel

```html
<!DOCTYPE html>
<html lang="en">
<head>
<meta charset="utf-8">
<title>VQ7 Online Marketing</title>
<link href="https://fonts.googleapis.com/css2?family=Montserrat:wght@400;600;700;800&family=Open+Sans:wght@400;600;700&display=swap" rel="stylesheet">
<style>
:root{
  --green:#3fd52e;
  --green-light:#6be85a;
  --ink:#111111;
  --text:#444444;
  --line:#cfcfcf;
  --dark:#0b0b0b;
  --cal:#c9d0dc;
  --badge:#2a2a2a;
}
*{box-sizing:border-box;margin:0;padding:0}
html,body{width:1200px;height:4776px;overflow:hidden}
body{font-family:"Open Sans",Arial,sans-serif;color:var(--text);background:#fff;position:relative}
h1,h2,h3,h4,.logo,.btn{font-family:"Montserrat",Arial,sans-serif}
.abs{position:absolute}
.btn{display:inline-block;background:var(--green);color:#fff;font-weight:700;font-size:15px;padding:14px 26px;border-radius:4px;letter-spacing:.5px}
.btn-sm{font-size:14px;padding:10px 22px}
.btn-outline{background:transparent;border:2px solid #fff}
.section-title{font-size:40px;font-weight:800;color:var(--ink);text-transform:uppercase;line-height:1.15}

/* top bar */
.topbar{top:0;left:0;width:1200px;height:104px;background:#fff;border-top:4px solid var(--green)}
.contact-item{top:28px;display:flex;gap:12px;align-items:center}
.contact-item .ico{width:28px;height:28px;border-radius:50%;background:var(--green);display:flex;align-items:center;justify-content:center}
.contact-item small{display:block;font-size:11px;font-weight:700;color:var(--ink);text-transform:uppercase}
.contact-item b{font-size:19px;color:var(--ink);font-weight:600}
.logo{font-weight:800;font-size:52px;color:var(--green);letter-spacing:2px;line-height:1}
.topbar .logo{left:0;width:1200px;text-align:center;top:18px}
.nav{top:104px;left:0;width:1200px;height:32px;background:var(--green);display:flex;justify-content:center;gap:78px;align-items:center}
.nav a{color:#fff;font-family:"Montserrat",sans-serif;font-weight:700;font-size:15px;text-decoration:none;text-transform:uppercase}

/* hero */
.hero{top:136px;left:0;width:1200px;height:584px;background:linear-gradient(90deg,#ffffff 0%,#f2f2f2 40%,#e6e6e6 100%)}
.hero-media{top:0;left:460px;width:740px;height:584px;background:linear-gradient(135deg,#dcdcdc,#f3f3f3 50%,#c9c9c9)}
.hero-text{top:140px;left:110px;width:560px}
.hero h1{font-size:62px;line-height:1.12;font-weight:800;color:var(--ink);text-transform:uppercase;margin-bottom:32px}
.scroll-down{top:700px;left:576px;width:44px;height:44px;border-radius:50%;background:#fff;border:2px solid var(--green);display:flex;align-items:center;justify-content:center}

/* values */
.values .section-title{top:826px;left:112px}
.value-card{top:904px;width:288px;height:272px;background:#fff;box-shadow:0 6px 26px rgba(0,0,0,.1);padding:40px 28px}
.value-card .ico{width:64px;height:64px;border-radius:50%;background:var(--green);display:flex;align-items:center;justify-content:center;margin-bottom:26px}
.value-card h4{font-size:20px;color:var(--ink);margin-bottom:8px}
.value-card p{font-size:14px;line-height:1.5}

/* ecommerce band */
.ecom{top:1380px;left:0;width:1200px;height:460px;background:linear-gradient(90deg,var(--green) 0%,var(--green-light) 100%)}
.ecom-text{top:68px;left:112px;width:580px;color:#fff}
.ecom h2{font-size:40px;line-height:1.15;font-weight:800;text-transform:uppercase;margin-bottom:18px}
.ecom p{font-size:15px;line-height:1.45;margin-bottom:28px}
.ecom-media{top:1200px;left:700px;width:500px;height:480px;background:linear-gradient(160deg,#e9e9e9,#ffffff 40%,#bfbfbf)}

/* marketing */
.marketing-media{top:1900px;left:120px;width:380px;height:400px;background:linear-gradient(180deg,#f0a46a 0%,#eaeaea 40%,#3a3a3a 100%)}
.marketing-text{top:1956px;left:608px;width:580px}
.marketing h2{font-size:40px;line-height:1.15;font-weight:800;color:var(--ink);text-transform:uppercase;margin-bottom:20px}
.marketing p{width:460px;font-size:15px;line-height:1.5;margin-bottom:20px}

/* team */
.team .section-title{top:2386px;left:0;width:1200px;text-align:center}
.team .lead{top:2446px;left:230px;width:740px;text-align:center;font-size:16px;line-height:1.5}
.team-band{top:2860px;left:0;width:1200px;height:300px;background:linear-gradient(180deg,var(--green) 0%,var(--green-light) 65%,#ffffff 100%)}
.team-photo{top:2540px;left:512px;width:568px;height:520px;background:linear-gradient(135deg,#d8d8d8,#9d9d9d 55%,#2a2f3a);border:10px solid #fff;box-shadow:0 6px 30px rgba(0,0,0,.12)}
.team-card{top:2600px;left:112px;width:400px;height:368px;background:#fff;box-shadow:0 6px 30px rgba(0,0,0,.12);padding:48px 40px}
.team-card h3{font-size:30px;font-weight:600;color:var(--ink);letter-spacing:1px;text-transform:uppercase}
.team-card .role{font-size:15px;color:var(--ink);margin:8px 0 22px}
.team-card p{font-size:15px;line-height:1.5}
.team-card a{display:inline-block;margin-top:10px;color:var(--green);font-weight:700;font-size:15px;text-decoration:underline}
.slider-controls{top:3008px;left:512px;display:flex;gap:4px}
.arrow-btn{width:48px;height:48px;background:var(--green);display:flex;align-items:center;justify-content:center;border:2px solid #fff}
.partners{top:3150px;left:180px;width:840px;display:flex;justify-content:space-between;align-items:center}
.partner{height:40px;background:var(--badge);border-radius:4px}
.carousel-arrows{top:3228px;left:0;width:1200px;display:flex;justify-content:center;gap:18px;font-size:26px;color:var(--ink);font-weight:700;line-height:1}

/* contact */
.contact-box{top:3272px;left:132px;width:348px;height:568px;background:var(--green);padding:60px 44px;color:#fff}
.contact-box h3{font-size:34px;font-weight:800;text-transform:uppercase;margin-bottom:40px}
.cb-row{display:flex;gap:18px;margin-bottom:40px;align-items:flex-start}
.cb-row .ico{flex:none;width:44px;height:44px;border-radius:50%;background:#fff;display:flex;align-items:center;justify-content:center}
.cb-row b{display:block;font-size:17px;margin-bottom:4px}
.cb-row span{font-size:14px;line-height:1.4}
.contact-form h3{top:3420px;left:532px;font-size:34px;font-weight:700;color:var(--ink);text-transform:uppercase}
.field{border-bottom:1px solid var(--line);font-size:14px;color:#555;padding-bottom:10px}

/* appointment */
.appoint .section-title{top:3914px;left:0;width:1200px;text-align:center;font-size:44px}
.appoint .lead{top:3980px;left:250px;width:700px;text-align:center;font-size:16px;line-height:1.5}
.footer{top:4440px;left:0;width:1200px;height:336px;background:var(--dark)}
.appt-card{top:4080px;left:120px;width:960px;height:520px;background:#fff;box-shadow:0 10px 40px rgba(0,0,0,.15)}
.calendar{top:4112px;left:140px;width:464px;height:456px;background:var(--cal);padding:30px 38px}
.cal-head{display:flex;justify-content:space-between;align-items:center;margin-bottom:18px}
.cal-head b{font-family:"Montserrat",sans-serif;font-size:30px;color:var(--ink);font-weight:600}
.cal-nav{display:flex;gap:12px}
.cal-nav span{width:40px;height:40px;background:var(--green);display:flex;align-items:center;justify-content:center}
.cal-grid{display:grid;grid-template-columns:repeat(7,1fr);row-gap:12px;text-align:center;font-size:26px;line-height:38px;color:var(--ink);font-family:"Montserrat",sans-serif}
.cal-grid .dow{font-weight:700;font-size:24px}
.cal-grid .off{color:#7c8594}
.cal-grid .sel{background:var(--green);color:#fff;margin:0 4px}
.cal-grid .alt{background:#a9e5a0;margin:0 4px}
.appt-form{top:4140px;left:644px;width:412px}
.appt-form .field{margin-bottom:30px}

/* footer */
.footer .logo{top:222px;left:130px;color:#fff;font-size:54px}
.footer-nav{top:232px;left:0;width:1200px;display:flex;justify-content:center;gap:34px}
.footer-nav a{color:#fff;font-family:"Montserrat",sans-serif;font-size:15px;font-weight:600;text-decoration:none;text-transform:uppercase}
.copyright{top:272px;left:0;width:1200px;text-align:center;color:#bbb;font-size:13px}
.socials{top:230px;left:940px;display:flex;gap:14px}
.socials span{width:20px;height:20px;border-radius:50%;background:#fff}
</style>
</head>
<body>

<header class="abs topbar">
  <div class="abs contact-item" style="left:110px">
    <span class="ico"><svg width="16" height="16" viewBox="0 0 24 24" fill="none" stroke="#fff" stroke-width="2.4"><rect x="3" y="5" width="18" height="14" rx="1"/><path d="M3 6l9 7 9-7"/></svg></span>
    <div><small>Email address</small><b>info@vq7.ch</b></div>
  </div>
  <div class="abs logo">VQ7</div>
  <div class="abs contact-item" style="left:884px">
    <span class="ico"><svg width="16" height="16" viewBox="0 0 24 24" fill="#fff"><path d="M6.6 10.8a15 15 0 006.6 6.6l2.2-2.2c.3-.3.7-.4 1-.2 1.1.4 2.3.6 3.6.6.6 0 1 .4 1 1V20c0 .6-.4 1-1 1C10.6 21 3 13.4 3 4c0-.6.4-1 1-1h3.5c.6 0 1 .4 1 1 0 1.3.2 2.5.6 3.6.1.3 0 .7-.2 1z"/></svg></span>
    <div><small>Phone number</small><b>+1-202-555-0184</b></div>
  </div>
</header>
<nav class="abs nav">
  <a>Home</a><a>eCommerce</a><a>Online Marketing</a><a>Integration</a><a>Company</a>
</nav>

<section class="abs hero">
  <div class="abs hero-media" role="img" aria-label="Desk with desktop monitor, laptop, tablet and phone showing an online shop"></div>
  <div class="abs hero-text">
    <h1>Welcome to VQ7 Online Marketing</h1>
    <span class="btn">GET STARTED</span>
  </div>
</section>
<div class="abs scroll-down"><svg width="20" height="20" viewBox="0 0 24 24" fill="none" stroke="#3fd52e" stroke-width="2.5"><path d="M6 9l6 6 6-6"/></svg></div>

<section class="values">
  <h2 class="abs section-title">Our Values</h2>
  <div class="abs value-card" style="left:112px">
    <div class="ico"><svg width="30" height="30" viewBox="0 0 24 24" fill="none" stroke="#fff" stroke-width="2"><circle cx="12" cy="12" r="8"/><path d="M12 4v16M4 12h16"/></svg></div>
    <h4>Sustainability</h4>
    <p>We build lasting solutions that keep growing with your shop and your team over the years.</p>
  </div>
  <div class="abs value-card" style="left:432px">
    <div class="ico"><svg width="30" height="30" viewBox="0 0 24 24" fill="none" stroke="#fff" stroke-width="2"><circle cx="12" cy="9" r="5"/><path d="M8 13l-2 8 6-3 6 3-2-8"/></svg></div>
    <h4>Quality</h4>
    <p>Every project is tested with care so your customers enjoy a fast and reliable experience.</p>
  </div>
  <div class="abs value-card" style="left:760px">
    <div class="ico"><svg width="30" height="30" viewBox="0 0 24 24" fill="none" stroke="#fff" stroke-width="2"><circle cx="12" cy="8" r="4"/><path d="M4 21c0-4 4-7 8-7s8 3 8 7"/></svg></div>
    <h4>Customer orientation</h4>
    <p>Your goals lead our work, with clear advice and direct contact from start to launch.</p>
  </div>
</section>

<section class="abs ecom">
  <div class="abs ecom-text">
    <h2>Your successful entry<br>into eCommerce</h2>
    <p>Do you want to sell your products or services online? But as an SME, don't you have a marketing department with e-commerce know-how? Then you will face a series of questions essential to the success of your web business crucial are. Which shop system is best suited to your goals?</p>
    <span class="btn btn-sm btn-outline">READ MORE</span>
  </div>
</section>
<div class="abs ecom-media" role="img" aria-label="Desktop monitor displaying an online shop"></div>

<section class="marketing">
  <div class="abs marketing-media" role="img" aria-label="Laptop with a rocket launching from the screen in a cloud of smoke"></div>
  <div class="abs marketing-text">
    <h2>Individual online<br>marketing solutions</h2>
    <p>In us you will find a dedicated team with passion, expertise and curiosity for all topics related to e-commerce and online marketing. Our agency brings you quickly, purposefully and economically with your products online.</p>
    <span class="btn btn-sm">READ MORE</span>
  </div>
</section>

<section class="team">
  <h2 class="abs section-title">Our VQ7 Team</h2>
  <p class="abs lead">We have many years of experience in software consulting. Our goal is to achieve the goals of our customers in a short time. We create added value and implement demanding requirements.</p>
  <div class="abs team-band"></div>
  <div class="abs team-photo" role="img" aria-label="Portrait of the eCommerce manager in a dark suit"></div>
  <div class="abs team-card">
    <h3>Lukas Brenner</h3>
    <div class="role">ECommerce Manager</div>
    <p>After studying business administration, I worked in marketing for a few years. After that, I worked in IT project management for many years. My focus is on project management, conception and implementation.</p>
    <a>Learn More</a>
  </div>
  <div class="abs slider-controls">
    <span class="arrow-btn"><svg width="16" height="16" viewBox="0 0 24 24" fill="none" stroke="#fff" stroke-width="3"><path d="M15 5l-7 7 7 7"/></svg></span>
    <span class="arrow-btn"><svg width="16" height="16" viewBox="0 0 24 24" fill="none" stroke="#fff" stroke-width="3"><path d="M9 5l7 7-7 7"/></svg></span>
  </div>
  <div class="abs partners">
    <span class="partner" style="width:150px" role="img" aria-label="Partner badge"></span>
    <span class="partner" style="width:90px" role="img" aria-label="Partner badge"></span>
    <span class="partner" style="width:230px" role="img" aria-label="Partner badge"></span>
    <span class="partner" style="width:120px" role="img" aria-label="Partner badge"></span>
  </div>
  <div class="abs carousel-arrows"><span>&lsaquo;</span><span>&rsaquo;</span></div>
</section>

<section class="contact">
  <div class="abs contact-box">
    <h3>Contact us</h3>
    <div class="cb-row">
      <span class="ico"><svg width="20" height="20" viewBox="0 0 24 24" fill="#3fd52e"><path d="M12 2a7 7 0 00-7 7c0 5 7 13 7 13s7-8 7-13a7 7 0 00-7-7zm0 9.5A2.5 2.5 0 1112 6.5a2.5 2.5 0 010 5z"/></svg></span>
      <span>Seestrasse 40, 8002 Zurich<br>Switzerland</span>
    </div>
    <div class="cb-row">
      <span class="ico"><svg width="20" height="20" viewBox="0 0 24 24" fill="#3fd52e"><path d="M6.6 10.8a15 15 0 006.6 6.6l2.2-2.2c.3-.3.7-.4 1-.2 1.1.4 2.3.6 3.6.6.6 0 1 .4 1 1V20c0 .6-.4 1-1 1C10.6 21 3 13.4 3 4c0-.6.4-1 1-1h3.5c.6 0 1 .4 1 1 0 1.3.2 2.5.6 3.6.1.3 0 .7-.2 1z"/></svg></span>
      <div><b>Call Us</b><span>+41 44 512 40 18</span></div>
    </div>
    <div class="cb-row">
      <span class="ico"><svg width="20" height="20" viewBox="0 0 24 24" fill="none" stroke="#3fd52e" stroke-width="2.4"><rect x="3" y="5" width="18" height="14" rx="1"/><path d="M3 6l9 7 9-7"/></svg></span>
      <div><b>Email Us</b><span>info@vq7.ch</span></div>
    </div>
  </div>
  <div class="contact-form">
    <h3 class="abs">Get in touch</h3>
    <div class="abs field" style="top:3500px;left:532px;width:250px">First Name</div>
    <div class="abs field" style="top:3500px;left:812px;width:260px">Last Name</div>
    <div class="abs field" style="top:3572px;left:532px;width:250px">Contact Number</div>
    <div class="abs field" style="top:3572px;left:812px;width:260px">Email Address</div>
    <div class="abs field" style="top:3636px;left:532px;width:540px;height:100px">Your Message Goes Here...</div>
    <span class="abs btn btn-sm" style="top:3756px;left:930px">SUBMIT NOW</span>
  </div>
</section>

<section class="appoint">
  <h2 class="abs section-title">Make an Appointment</h2>
  <p class="abs lead">There are many variations of passages of Lorem Ipsum available, but the majority have suffered alteration in some form, by injected humour, or randomised words.</p>
  <div class="abs footer">
    <div class="abs logo">VQ7</div>
    <div class="abs footer-nav"><a>Home</a><a>About Us</a><a>Blog</a><a>Contact Us</a><a>History</a></div>
    <div class="abs socials"><span></span><span></span><span></span><span></span><span></span></div>
    <div class="abs copyright">Copyright &copy; 2023 vq7.ch | All Rights Reserved</div>
  </div>
  <div class="abs appt-card"></div>
  <div class="abs calendar">
    <div class="cal-head">
      <b>January 2023</b>
      <div class="cal-nav">
        <span><svg width="16" height="16" viewBox="0 0 24 24" fill="none" stroke="#fff" stroke-width="3"><path d="M15 5l-7 7 7 7"/></svg></span>
        <span><svg width="16" height="16" viewBox="0 0 24 24" fill="none" stroke="#fff" stroke-width="3"><path d="M9 5l7 7-7 7"/></svg></span>
      </div>
    </div>
    <div class="cal-grid">
      <span class="dow">Mo</span><span class="dow">Tu</span><span class="dow">We</span><span class="dow">Th</span><span class="dow">Fr</span><span class="dow">Sa</span><span class="dow">Su</span>
      <span class="off">26</span><span class="off">27</span><span class="off">28</span><span class="off">29</span><span class="off">30</span><span class="off">31</span><span>1</span>
      <span>2</span><span>3</span><span>4</span><span>5</span><span>6</span><span>7</span><span>8</span>
      <span>9</span><span>10</span><span class="sel">11</span><span class="alt">12</span><span class="sel">13</span><span class="sel">14</span><span>15</span>
      <span>16</span><span>17</span><span>18</span><span>19</span><span>20</span><span>21</span><span>22</span>
      <span>23</span><span>24</span><span>25</span><span>26</span><span>27</span><span>28</span><span>29</span>
      <span>30</span><span>31</span>
    </div>
  </div>
  <div class="abs appt-form">
    <div class="field">First Name</div>
    <div class="field">Last Name</div>
    <div class="field">Contact Number</div>
    <div class="field">Email Address</div>
    <div class="field" style="height:80px">Your Message Goes Here...</div>
  </div>
  <span class="abs btn btn-sm" style="top:4520px;left:916px">SUBMIT NOW</span>
</section>

</body>
</html>
```